Brolga Ridge Earthmoving & Transport Business Card

Can you please design a business card for an Earthworks, Haulage truck and machinery hire company. They also provide sand soil and mulch supply, as well as screening of products. Can you re-create the logo from the attached but add Brolga Ridge Earthmoving & Transport just use the three diamond design.

Target Market(s)

Earthmoving and Transport, Landscapers, Construction

Contact Information for Business Card

ABN 52 907 338 214, Dale Pettigrew, Managing Director, Brolga Ridge Earthmoving & Transport Mobile 0438 256 904 Email brgtransport2011@haulmail.example

Font styles to use
Sans Serif

Colors
ec1f27
000000
cbcbcb
ffffff

Requirements
Must have
• Listed on the back, Earthworks | Haulage | Truck and Machinery Hire | Sand, Soil & Mulch Supply | Screening of Products
Nice to have
• Would be good for it to look appealing to a mans man, because it relates to heavy machinery, earthworks, construction etc. Black, red and white would be good maybe with a bit of silver somewhere.
Should not have
• not sure

```html
<!DOCTYPE html>
<html lang="en">
<head>
<meta charset="utf-8">
<title>Brolga Ridge Earthmoving &amp; Transport – Business Card</title>
<link rel="stylesheet" href="https://fonts.googleapis.com/css2?family=Saira:wght@400;500;600;700&display=swap">
<style>
  :root {
    --red: #ec1f27;
    --red-mid: #a8161d;
    --red-deep: #7a0b10;
    --red-dark: #4f0609;
    --machine: #2a0406;
    --ground: #231f20;
    --black: #000000;
    --silver: #cbcbcb;
    --white: #ffffff;
    --backdrop: #d8d0bf;
  }
  * { margin: 0; padding: 0; box-sizing: border-box; }
  html, body { width: 1199px; height: 1200px; overflow: hidden; }
  body {
    background: var(--backdrop);
    font-family: "Saira", sans-serif;
    position: relative;
  }
  .card {
    position: absolute;
    left: 80px;
    width: 1040px;
    height: 560px;
    overflow: hidden;
    box-shadow: 0 12px 30px rgba(0,0,0,0.35);
  }
  .card-front { top: 30px; }
  .card-back { top: 620px; }
  .card-art { position: absolute; inset: 0; width: 100%; height: 100%; }

  .brand-mark {
    position: absolute;
    display: flex;
    align-items: center;
    gap: 20px;
  }
  .brand-mark .mark-square {
    width: 70px; height: 70px;
    background: var(--white);
  }
  .brand-mark .mark-name {
    font-weight: 700;
    font-size: 96px;
    line-height: 1;
    color: var(--white);
    letter-spacing: 6px;
  }

  /* front */
  .front-brand { left: 120px; top: 80px; }
  .front-tagline {
    position: absolute;
    left: 150px; top: 225px;
    font-weight: 600;
    font-size: 42px;
    line-height: 1.15;
    color: var(--ground);
    text-align: center;
  }
  .machine-scene {
    position: absolute;
    left: 600px; top: 90px;
    width: 420px; height: 300px;
    background: radial-gradient(closest-side at 50% 62%, rgba(42,4,6,0.9) 0%, rgba(42,4,6,0.55) 50%, rgba(42,4,6,0) 100%);
  }
  .front-contact {
    position: absolute;
    left: 0; right: 0; top: 425px;
    text-align: center;
    color: var(--silver);
  }
  .front-contact .phone {
    font-weight: 700;
    font-size: 44px;
    letter-spacing: 2px;
  }
  .front-contact .email {
    font-weight: 500;
    font-size: 26px;
    letter-spacing: 4px;
    margin-top: 2px;
  }

  /* back */
  .back-slogan {
    position: absolute;
    left: 60px; width: 520px; top: 50px;
    text-align: center;
    color: var(--white);
    font-weight: 500;
    font-size: 38px;
    line-height: 1.35;
  }
  .back-brand { left: 165px; top: 205px; }
  .back-tagline {
    position: absolute;
    left: 60px; width: 520px; top: 345px;
    text-align: center;
    color: var(--white);
    font-weight: 600;
    font-size: 40px;
    line-height: 1.2;
  }
  .contact-block {
    position: absolute;
    left: 600px; width: 420px; top: 150px;
    text-align: center;
  }
  .contact-block .person-name {
    font-weight: 700;
    font-size: 46px;
    line-height: 1;
    color: var(--silver);
  }
  .contact-block .person-role {
    font-weight: 500;
    font-size: 27px;
    letter-spacing: 3px;
    color: var(--white);
    margin-top: 6px;
  }
  .contact-block .person-phone {
    font-weight: 700;
    font-size: 42px;
    color: var(--white);
    letter-spacing: 2px;
    margin-top: 12px;
  }
  .contact-block .abn {
    font-weight: 400;
    font-size: 31px;
    line-height: 1.35;
    color: var(--silver);
    margin-top: 16px;
  }
  .service-list {
    position: absolute;
    left: 20px; right: 20px; top: 508px;
    display: flex;
    justify-content: center;
    flex-wrap: nowrap;
    gap: 10px;
    list-style: none;
    font-weight: 500;
    font-size: 18px;
    color: var(--silver);
    white-space: nowrap;
  }
  .service-list li + li::before {
    content: "|";
    margin-right: 10px;
    color: var(--white);
  }
</style>
</head>
<body>

<section class="card card-front" aria-label="Business card front">
  <svg class="card-art" viewBox="0 0 1040 560" preserveAspectRatio="none" aria-hidden="true">
    <rect width="1040" height="560" fill="var(--red-mid)"/>
    <polygon points="540,0 1040,0 1040,560 760,560" fill="var(--red-deep)"/>
    <polygon points="720,0 1040,0 1040,300" fill="var(--red-dark)" opacity="0.55"/>
    <polygon points="0,0 540,0 300,560 0,560" fill="var(--red)" opacity="0.25"/>
  </svg>
  <div class="machine-scene" role="img" aria-label="Silhouette of an excavator working on a dirt mound"></div>
  <svg class="card-art" viewBox="0 0 1040 560" preserveAspectRatio="none" aria-hidden="true">
    <path d="M0,380 C120,370 220,372 330,380 C430,388 560,392 640,378 C700,368 730,350 800,352 C880,354 940,352 1040,338 L1040,560 L0,560 Z" fill="var(--ground)"/>
  </svg>
  <div class="brand-mark front-brand">
    <span class="mark-square"></span>
    <span class="mark-name">BRG</span>
  </div>
  <div class="front-tagline">Earthmoving &amp;<br>Transport</div>
  <div class="front-contact">
    <div class="phone">0438 256 904</div>
    <div class="email">brgtransport2011@haulmail.example</div>
  </div>
</section>

<section class="card card-back" aria-label="Business card back">
  <svg class="card-art" viewBox="0 0 1040 560" preserveAspectRatio="none" aria-hidden="true">
    <rect width="1040" height="560" fill="var(--red-mid)"/>
    <polygon points="0,150 380,0 640,0 0,430" fill="var(--red-deep)" opacity="0.45"/>
    <polygon points="0,430 640,0 500,560 0,560" fill="var(--red)" opacity="0.2"/>
    <polygon points="640,0 1040,0 1040,560 480,560" fill="var(--red-dark)"/>
    <polygon points="820,0 1040,0 1040,340" fill="var(--red-deep)" opacity="0.6"/>
    <polygon points="700,560 1040,380 1040,560" fill="var(--red-mid)" opacity="0.5"/>
  </svg>
  <div class="back-slogan">For all your<br>transport needs</div>
  <div class="brand-mark back-brand">
    <span class="mark-square"></span>
    <span class="mark-name">BRG</span>
  </div>
  <div class="back-tagline">Earthmoving &amp;<br>Transport</div>
  <div class="contact-block">
    <div class="person-name">DALE PETTIGREW</div>
    <div class="person-role">MANAGING DIRECTOR</div>
    <div class="person-phone">0438 256 904</div>
    <div class="abn">ABN 52<br>907 338 214</div>
  </div>
  <ul class="service-list">
    <li>Earthworks</li>
    <li>Haulage</li>
    <li>Truck and Machinery Hire</li>
    <li>Sand, Soil &amp; Mulch Supply</li>
    <li>Screening of Products</li>
  </ul>
</section>

</body>
</html>
```